Accredited Quality Product Website

WEBSITE
Require a website and logo for a product website. All registered products will comply with a set of pre-defined criteria. The criteria have been developed to ensure only products of a very high quality which are produced in a socially and environmentally sustainable manner are registered.
The site will developed in a number of stages.
Stage 1: link products to external website via standard and affiliate links.
Stage 2: Stage 1 links and ecommerce sales.
This project is for Stage 1 only.
Example Pages: Home Page, Products, Submit a Product, Evaluation Criteria, Contact Us, About Us, Refund Policy, Privacy Policy, Copyright, Newsletter Signup, ...
A Functional Specification to assist with the design and development will be provided to the shortlisted designs.
LOGO
We like RVX font used on Halvorn Stadt.
Possibly consider TE inside a circle.
The logo will need to be provided in three colour schemes and black and white.
We have no colour scheme set. We do however like green, blue, silver, orange.
TERVO
Coded - Design and coding required
5+ page

```html
<!DOCTYPE html>
<html lang="en">
<head>
<meta charset="utf-8">
<title>TERVO — Accredited Quality Products</title>
<link rel="stylesheet" href="https://fonts.googleapis.com/css2?family=Montserrat:wght@400;500;600;700&family=Exo+2:wght@600;700&family=PT+Serif&display=swap">
<style>
:root{
  --bg:#1b1b1b;
  --header:#1d1d1d;
  --panel:#2a2a2a;
  --band:#262626;
  --orange:#f4a300;
  --blue:#1b6fd0;
  --white:#ffffff;
  --muted:#bdbdbd;
  --ink:#222222;
  --line:#3a3a3a;
}
*{margin:0;padding:0;box-sizing:border-box}
html,body{width:1200px;height:3888px;overflow:hidden}
body{background:var(--bg);font-family:"Montserrat",sans-serif;color:var(--white);position:relative}
.abs{position:absolute}

/* header */
.site-header{position:absolute;left:0;top:0;width:1200px;height:143px;background:var(--header)}
.brand{position:absolute;display:flex;align-items:center;gap:12px}
.brand-mark{border:4px solid var(--orange);border-radius:50%}
.brand-name{font-family:"Montserrat",sans-serif;font-weight:500;color:var(--white);letter-spacing:1px}
.site-header .brand{left:136px;top:26px}
.site-header .brand-mark{width:90px;height:90px}
.site-header .brand-name{font-size:40px}
.search{left:594px;top:30px;width:184px;height:28px;background:var(--white);font-size:10px;color:#333;padding:8px 10px;font-weight:600}
.search svg{position:absolute;right:8px;top:8px}
.account{left:827px;top:36px;font-size:13px;color:var(--white)}
.cart{left:975px;top:30px;display:flex;gap:10px;font-size:11px;line-height:15px}
.cart b{font-weight:600}
.main-nav{left:467px;top:94px;display:flex;gap:0;font-size:13px;font-weight:600}
.main-nav a{color:var(--white);text-decoration:none;padding:6px 12px;margin-right:16px}
.main-nav a.active{background:var(--orange)}

/* hero */
.hero{left:0;top:143px;width:1200px;height:600px}
.hero-title{left:663px;top:312px;font-family:"Montserrat",sans-serif;font-weight:700;font-size:36px;line-height:50px;color:var(--blue)}
.btn{background:var(--orange);color:var(--white);font-weight:700;text-align:center;text-transform:uppercase}
.hero-btn{left:666px;top:433px;width:153px;height:40px;line-height:40px;font-size:14px}
.slide-arrows{left:1008px;top:617px;display:flex;gap:4px}
.slide-arrows span{width:28px;height:28px;background:#3a3a3a;display:flex;align-items:center;justify-content:center}

/* features */
.features{left:135px;top:777px;width:930px;height:169px;background:var(--panel);display:flex;padding:38px 0 0 38px}
.feature{width:250px;display:flex;gap:10px}
.feature h4{font-size:12px;font-weight:600;margin-bottom:8px}
.feature p{font-size:10px;line-height:14px;color:var(--muted);width:170px}
.feature a{display:block;margin-top:12px;font-size:10px;font-weight:700;color:var(--orange)}
.stars{color:var(--orange);font-size:12px;letter-spacing:1px}

/* sections */
.section-title{width:1200px;left:0;text-align:center;font-family:"Exo 2",sans-serif;font-weight:700;font-size:25px}
.carousel-arrow{position:absolute}
.product{position:absolute;width:225px;height:311px;background:var(--white);color:var(--ink)}
.product .shot{position:absolute;left:42px;top:22px;width:141px;height:160px;border-radius:8px}
.product h5{position:absolute;left:24px;top:206px;font-family:"PT Serif",serif;font-weight:400;font-size:13px}
.product p{position:absolute;left:24px;top:228px;font-size:10px;color:#555}
.product .price{position:absolute;left:24px;top:256px;font-size:20px;font-weight:700}
.product .buy{position:absolute;left:114px;top:256px;width:92px;height:28px;line-height:28px;font-size:10px}

/* product of week */
.feature-banner{left:135px;top:1498px;width:930px;height:358px}
.banner-copy{left:177px;top:1588px;width:250px}
.banner-copy h3{font-family:"Exo 2",sans-serif;font-weight:700;font-size:27px;line-height:31px}
.banner-copy p{margin-top:14px;font-size:10px;line-height:13px;color:#e0e0e0;width:185px}
.banner-copy .btn{margin-top:14px;width:120px;height:32px;line-height:32px;font-size:13px}

/* reviews */
.review{position:absolute;width:202px}
.review .shot{width:202px;height:163px}
.review .stars{margin-top:14px}
.review h5{margin-top:6px;font-size:13px;font-weight:700}
.review p{margin-top:8px;font-size:10px;line-height:14px;color:#cfcfcf}
.review .more{margin-top:6px;font-size:10px;font-weight:700;color:var(--orange)}
.reviewer{margin-top:18px;display:flex;align-items:center;gap:8px;font-size:10px;font-weight:700}
.reviewer span{width:26px;height:26px;border-radius:50%;background:#8a8a8a;border:2px solid #ddd}

/* newsletter */
.newsletter{left:0;top:3066px;width:1200px;height:438px;background:var(--band)}
.newsletter .shot{position:absolute;left:0;top:0;width:518px;height:438px}
.newsletter h3{position:absolute;left:648px;top:104px;font-size:22px;font-weight:700;letter-spacing:1px}
.newsletter .lead{position:absolute;left:648px;top:136px;font-size:14px}
.newsletter .field{position:absolute;left:648px;top:192px;width:355px;height:52px;background:var(--white);color:#555;font-size:11px;padding:19px 18px}
.newsletter .btn{position:absolute;left:648px;top:270px;width:104px;height:34px;line-height:34px;font-size:14px}

/* footer */
.site-footer{left:0;top:3504px;width:1200px;height:384px;background:var(--header)}
.site-footer .brand{left:171px;top:99px}
.site-footer .brand-mark{width:104px;height:104px}
.site-footer .brand-name{font-size:44px}
.footer-col{position:absolute;top:74px;font-size:11px;line-height:18px}
.footer-col h6{font-size:12px;font-weight:700;margin-bottom:18px}
.contact-row{display:flex;gap:12px;align-items:flex-start;margin-bottom:16px;color:#e6e6e6}
.menu-list li{list-style:none;font-size:11px;line-height:17px;color:#e6e6e6}
.social-row{display:flex;align-items:center;gap:10px;margin-bottom:14px;font-size:11px}
.social-row span{width:26px;height:26px;border-radius:50%;background:var(--blue)}
.footer-rule{left:135px;top:286px;width:930px;height:1px;background:var(--line)}
.copyright{left:0;top:326px;width:1200px;text-align:center;font-size:11px;color:#dcdcdc}
</style>
</head>
<body>

<header class="site-header">
  <div class="brand"><span class="brand-mark"></span><span class="brand-name">TERVO</span></div>
  <div class="abs search">SEARCH PRODUCTS
    <svg width="11" height="11" viewBox="0 0 11 11"><circle cx="4.5" cy="4.5" r="3.5" fill="none" stroke="#333" stroke-width="1.4"/><line x1="7.2" y1="7.2" x2="10" y2="10" stroke="#333" stroke-width="1.4"/></svg>
  </div>
  <div class="abs account">Login &nbsp;/&nbsp; Register</div>
  <div class="abs cart">
    <svg width="28" height="24" viewBox="0 0 28 24"><path d="M1 3h5l3 12h13l3-9H8" fill="none" stroke="#fff" stroke-width="2"/><circle cx="11" cy="20" r="2" fill="#fff"/><circle cx="20" cy="20" r="2" fill="#fff"/><circle cx="22" cy="4" r="4" fill="var(--orange)"/></svg>
    <div>MY CART<br><b>$0.00</b></div>
  </div>
  <nav class="abs main-nav">
    <a class="active">HOME</a><a>ABOUT US</a><a>SERVICES</a><a>PRODUCTS</a><a>BLOG</a><a>CONTACT US</a>
  </nav>
</header>

<section class="abs hero">
  <svg width="1200" height="600" viewBox="0 0 1200 600" role="img" aria-label="Flat-lay of denim, leather wallet, watch, glasses, belt, passport and checked shirt on a white wooden table">
    <defs>
      <linearGradient id="heroTone" x1="0" y1="0" x2="1" y2="0">
        <stop offset="0" stop-color="#4a4d55"/>
        <stop offset=".35" stop-color="#8a8e96"/>
        <stop offset=".6" stop-color="#e8e8e6"/>
        <stop offset="1" stop-color="#f2f2f0"/>
      </linearGradient>
    </defs>
    <rect width="1200" height="600" fill="url(#heroTone)"/>
    <path d="M0 560 Q600 500 1200 540 L1200 600 L0 600Z" fill="var(--bg)"/>
    <path d="M0 548 Q600 488 1200 528" fill="none" stroke="var(--orange)" stroke-width="12"/>
  </svg>
</section>
<h1 class="abs hero-title">Responsible Products<br>Reliable Luxury</h1>
<div class="abs btn hero-btn">Shop Now</div>
<div class="abs slide-arrows">
  <span><svg width="8" height="10"><path d="M6 1 2 5l4 4" fill="none" stroke="#fff" stroke-width="2"/></svg></span>
  <span><svg width="8" height="10"><path d="M2 1l4 4-4 4" fill="none" stroke="#fff" stroke-width="2"/></svg></span>
</div>

<section class="abs features">
  <div class="feature"><div><div class="stars">★★★★★</div><p style="margin-top:6px">Lorem ipsum dolor sit amet, consectetur adipiscing</p><a>See Ratings</a></div></div>
  <div class="feature">
    <svg width="28" height="34" viewBox="0 0 28 34"><circle cx="14" cy="12" r="10" fill="none" stroke="var(--orange)" stroke-width="3"/><circle cx="14" cy="12" r="4" fill="var(--orange)"/><path d="M8 20l-3 12 9-4 9 4-3-12" fill="var(--orange)"/></svg>
    <div><h4>Guaranteed Accurate</h4><p>Lorem ipsum dolor sit amet, consectetur adipiscing</p><a>Read More</a></div>
  </div>
  <div class="feature">
    <svg width="34" height="26" viewBox="0 0 34 26"><path d="M17 24C6 22 2 12 2 4c9 0 15 8 15 20zM17 24c11-2 15-12 15-20-9 0-15 8-15 20z" fill="var(--orange)"/></svg>
    <div><h4>Organically Certified</h4><p>Lorem ipsum dolor sit amet, consectetur adipiscing</p><a>Read More</a></div>
  </div>
  <div class="feature">
    <svg width="30" height="28" viewBox="0 0 30 28"><path d="M3 14l9 9L27 4" fill="none" stroke="var(--orange)" stroke-width="5"/></svg>
    <div><h4>Quality Guarantee</h4><p>Lorem ipsum dolor sit amet, consectetur adipiscing</p><a>Read More</a></div>
  </div>
</section>

<h2 class="abs section-title" style="top:1000px">New Arrivals</h2>
<svg class="carousel-arrow" style="left:80px;top:1216px" width="22" height="56"><path d="M20 2 3 28l17 26" fill="none" stroke="#777" stroke-width="2"/></svg>
<svg class="carousel-arrow" style="left:1098px;top:1216px" width="22" height="56"><path d="M2 2l17 26L2 54" fill="none" stroke="#777" stroke-width="2"/></svg>

<article class="product" style="left:135px;top:1091px"><div class="shot" role="img" aria-label="Steam iron" style="background:linear-gradient(135deg,#f4eef6,#c99ad2)"></div><h5>PRODUCT TITLE</h5><p>Alamcorper est eget tempor cursus</p><div class="price">$25.99</div><div class="btn buy">Buy Now</div></article>
<article class="product" style="left:371px;top:1091px"><div class="shot" role="img" aria-label="Folded blue jeans" style="background:linear-gradient(135deg,#dfe7f0,#3d6c9c)"></div><h5>PRODUCT TITLE</h5><p>Alamcorper est eget tempor cursus</p><div class="price">$25.99</div><div class="btn buy">Buy Now</div></article>
<article class="product" style="left:607px;top:1091px"><div class="shot" role="img" aria-label="Tan leather shoulder bag" style="background:linear-gradient(135deg,#f6ece0,#c77a33)"></div><h5>PRODUCT TITLE</h5><p>Alamcorper est eget tempor cursus</p><div class="price">$25.99</div><div class="btn buy">Buy Now</div></article>
<article class="product" style="left:842px;top:1091px"><div class="shot" role="img" aria-label="Mosaic glass candle holder" style="background:linear-gradient(135deg,#eee9e2,#5a3a2a)"></div><h5>PRODUCT TITLE</h5><p>Alamcorper est eget tempor cursus</p><div class="price">$25.99</div><div class="btn buy">Buy Now</div></article>

<div class="abs feature-banner" role="img" aria-label="Living room with wall-mounted television, speakers and wooden media cabinet" style="background:linear-gradient(90deg,#3b3a36 0%,#6b665c 30%,#c8bca6 60%,#8a7b66 100%)"></div>
<div class="abs banner-copy">
  <h3>TERVO Product<br>of the Week</h3>
  <p>Sed ut perspiciatis unde omnis iste natus error sit voluptatem accusantium doloremque laudantium.</p>
  <div class="btn">Shop Now</div>
</div>

<h2 class="abs section-title" style="top:1972px">Popular Products</h2>
<svg class="carousel-arrow" style="left:80px;top:2201px" width="22" height="56"><path d="M20 2 3 28l17 26" fill="none" stroke="#777" stroke-width="2"/></svg>
<svg class="carousel-arrow" style="left:1098px;top:2201px" width="22" height="56"><path d="M2 2l17 26L2 54" fill="none" stroke="#777" stroke-width="2"/></svg>

<article class="product" style="left:135px;top:2074px"><div class="shot" role="img" aria-label="Folded checked shirt" style="background:linear-gradient(135deg,#e7e9f0,#2c3556)"></div><h5>PRODUCT TITLE</h5><p>Alamcorper est eget tempor cursus</p><div class="price">$25.99</div><div class="btn buy">Buy Now</div></article>
<article class="product" style="left:371px;top:2074px"><div class="shot" role="img" aria-label="Canister vacuum cleaner" style="background:linear-gradient(135deg,#f0eeee,#b3262e)"></div><h5>PRODUCT TITLE</h5><p>Alamcorper est eget tempor cursus</p><div class="price">$25.99</div><div class="btn buy">Buy Now</div></article>
<article class="product" style="left:607px;top:2074px"><div class="shot" role="img" aria-label="Electric hair trimmer" style="background:linear-gradient(135deg,#f2f2f2,#2b2b2b)"></div><h5>PRODUCT TITLE</h5><p>Alamcorper est eget tempor cursus</p><div class="price">$25.99</div><div class="btn buy">Buy Now</div></article>
<article class="product" style="left:842px;top:2074px"><div class="shot" role="img" aria-label="Stacked plates and green mug" style="background:linear-gradient(135deg,#eef2e2,#4f8a3a)"></div><h5>PRODUCT TITLE</h5><p>Alamcorper est eget tempor cursus</p><div class="price">$25.99</div><div class="btn buy">Buy Now</div></article>

<h2 class="abs section-title" style="top:2492px;font-size:20px;letter-spacing:1px">PRODUCT REVIEWS</h2>

<article class="review" style="left:130px;top:2600px"><div class="shot" role="img" aria-label="Living room with television cabinet" style="background:linear-gradient(135deg,#e9e6df,#8a9aa8)"></div><div class="stars">★★★★★</div><h5>Lorem Ipsum is simply du</h5><p>There are many variations of passages of Lorem Ipsum available, but the majority have suffered alteration.</p><div class="more">MORE</div><div class="reviewer"><span></span>RICHARD</div></article>
<article class="review" style="left:373px;top:2600px"><div class="shot" role="img" aria-label="Smartphone and red headphones" style="background:linear-gradient(135deg,#2a2a2a,#8b1e24)"></div><div class="stars">★★★★★</div><h5>Lorem Ipsum is simply du</h5><p>There are many variations of passages of Lorem Ipsum available, but the majority have suffered alteration.</p><div class="more">MORE</div><div class="reviewer"><span></span>MARK</div></article>
<article class="review" style="left:617px;top:2600px"><div class="shot" role="img" aria-label="Sneakers, towel and dumbbells on wood" style="background:linear-gradient(135deg,#6d655c,#d94a86)"></div><div class="stars">★★★★★</div><h5>Lorem Ipsum is simply du</h5><p>There are many variations of passages of Lorem Ipsum available, but the majority have suffered alteration.</p><div class="more">MORE</div><div class="reviewer"><span></span>FERANDO</div></article>
<article class="review" style="left:863px;top:2600px"><div class="shot" role="img" aria-label="Folded dress shirts" style="background:linear-gradient(135deg,#c9cbe0,#4c4f82)"></div><div class="stars">★★★★★</div><h5>Lorem Ipsum is simply du</h5><p>There are many variations of passages of Lorem Ipsum available, but the majority have suffered alteration.</p><div class="more">MORE</div><div class="reviewer"><span></span>RICHARD</div></article>

<section class="abs newsletter">
  <div class="shot" role="img" aria-label="Stack of folded blue striped shirts" style="background:linear-gradient(160deg,#2f4fa8,#1a2f78 60%,#b8c2d6)"></div>
  <h3>NEWSLETTER</h3>
  <div class="lead">Get more details to signup</div>
  <div class="field">E-mail Id</div>
  <div class="btn">Signup</div>
</section>

<footer class="abs site-footer">
  <div class="brand"><span class="brand-mark"></span><span class="brand-name">TERVO</span></div>
  <div class="footer-col" style="left:495px">
    <h6>CONTACT US</h6>
    <div class="contact-row"><svg width="10" height="14" viewBox="0 0 10 14"><path d="M5 13S1 8 1 5a4 4 0 0 1 8 0c0 3-4 8-4 8z" fill="#fff"/></svg><div>1180 Linden Hollow Rd<br>Brookfield, WA</div></div>
    <div class="contact-row"><svg width="12" height="12" viewBox="0 0 12 12"><path d="M2 1l3 3-1.5 1.5a7 7 0 0 0 3 3L8 7l3 3-2 2C5 12 0 7 0 3z" fill="#fff"/></svg><div>555.014.2207</div></div>
    <div class="contact-row"><svg width="13" height="10" viewBox="0 0 13 10"><rect x=".5" y=".5" width="12" height="9" fill="#fff"/><path d="M.5 .5l6 5 6-5" fill="none" stroke="#1d1d1d"/></svg><div>info@tervo.com</div></div>
  </div>
  <div class="footer-col" style="left:741px">
    <h6>MENU</h6>
    <ul class="menu-list"><li>HOME</li><li>ABOUT US</li><li>SERVICES</li><li>PRODUCTS</li><li>BLOG</li><li>TESTIMONIALS</li><li>CONTACT US</li></ul>
  </div>
  <div class="footer-col" style="left:938px">
    <h6>CONNECT WITH US</h6>
    <div class="social-row"><span></span>Friendwall</div>
    <div class="social-row"><span></span>Chirper</div>
    <div class="social-row"><span style="background:#2b2b2b"></span>Workline</div>
  </div>
  <div class="abs footer-rule"></div>
  <div class="abs copyright">Copyrights @ 2018 All Rights Reserved</div>
</footer>

</body>
</html>
```